Solvane Glow LED - E- Commerce site

We need a website designed for an LED Billboard company that sells:
1) LED Billboards (Sales & Rental)
2) LED Gas Station lights
3) Truss Systems (Sales & Rental)
4) Sound Systems (Sales & Rental)

Attached are websites that sell similar products as Solvane Glow LED. Target market is for business, property managers and event coordinators.
This site will need to be an e-commerce site where customers can purchase the product directly from the site. What I'm looking for is a design layout to start.

Conceptual Web Designs:
http://example-panelora.test/index.html
http://www.vormpix.com/
http://www.droneplayaudio.com/
http://www.quillmarkdisplay.com/

Attached is the logo of the company: Please note that the new spelling of the logo is "Solvane Glow LED" using domain " SolvaneGlowLED.com

Industry/Entity Type

Gas Station

Number of Pages Required

5+ page

Requirements
Must have
• 1) E-Commerce - Customers will need to be able to order product from the site.
• 2) Customers will also have the option to rent the product as well.
Nice to have
• I like the image of the attached website, that has a video clip loop
• http://www.quillmarkdisplay.com/

```html
<!DOCTYPE html>
<html lang="en">
<head>
<meta charset="utf-8">
<title>Solvane Glow LED – One Stop Shop</title>
<link rel="stylesheet" href="https://fonts.googleapis.com/css2?family=Questrial&family=Jost:wght@400;500;600&display=swap">
<style>
:root{
  --ink:#222;
  --muted:#666;
  --line:#dcdcdc;
  --brand-green:#3ba846;
  --brand-green-dark:#2b8a35;
  --blue:#1e56a6;
  --blue-dark:#17447f;
  --green:#3aa946;
  --green-dark:#2a8a35;
  --yellow:#f7c417;
  --yellow-dark:#e6a90e;
  --red:#e3262d;
  --red-dark:#c51d23;
  --pink:#e0176f;
  --accent-red:#e8282f;
  --gold:#f2c300;
  --black:#1b1b1b;
  --footer:#ededed;
}
*{box-sizing:border-box;margin:0;padding:0}
html,body{width:1200px;height:2875px;overflow:hidden}
body{font-family:"Questrial",Arial,sans-serif;color:var(--ink);background:#fff;font-size:14px}
h1,h2,h3,h4,.heading{font-family:"Jost",Arial,sans-serif;font-weight:500}
a{color:inherit;text-decoration:none}
.container{width:1052px;margin:0 auto;position:relative}

/* header */
.site-header{height:138px;position:relative}
.brand{position:absolute;left:74px;top:34px;display:flex;align-items:center;gap:12px}
.brand-dot{width:40px;height:40px;border-radius:50%;background:var(--gold)}
.brand-name{font-family:"Jost",sans-serif;font-weight:600;font-size:26px;color:var(--gold)}
.welcome{position:absolute;left:242px;top:16px;font-size:13px;color:#333}
.top-links{position:absolute;right:74px;top:16px;font-size:13px;color:#333}
.top-links span{margin:0 6px;color:#999}
.call{position:absolute;left:772px;top:64px;display:flex;gap:10px;align-items:center}
.call small{display:block;font-size:12px;color:#777}
.call strong{font-size:17px;font-weight:400}
.cart{position:absolute;right:74px;top:52px;width:182px;height:62px;background:var(--brand-green);border:1px solid var(--brand-green-dark);color:#fff;display:flex;align-items:center;gap:10px;padding:0 12px}
.cart b{font-family:"Jost",sans-serif;font-weight:500;font-size:17px;display:block}
.cart small{font-size:13px}

.main-nav{height:40px;border-top:1px solid var(--line);border-bottom:1px solid var(--line);position:relative}
.main-nav ul{list-style:none;display:flex;position:absolute;left:74px;top:0;height:38px}
.main-nav li{padding:0 20px;line-height:38px;font-size:14px;color:#444}
.main-nav li.active{background:#e6e6e6}
.search{position:absolute;right:74px;top:0;width:244px;height:38px;background:#eee;display:flex;align-items:center;justify-content:space-between;padding:0 14px;color:#aaa;font-size:13px}

/* hero */
.hero{height:547px;position:relative;overflow:hidden}
.hero-photo{position:absolute;inset:0;background:linear-gradient(180deg,#2d2f34 0%,#4a4c52 45%,#9a9792 70%,#5a5854 100%)}
.hero-title{position:absolute;top:62px;width:100%;text-align:center;color:#fff;font-family:"Jost",sans-serif;font-size:56px;font-weight:500;letter-spacing:1px}
.hero-sub{position:absolute;top:128px;width:100%;display:flex;justify-content:center;align-items:center;gap:14px;color:var(--gold);font-family:"Jost",sans-serif;font-size:40px;font-weight:500}
.hero-sub i{display:block;width:46px;height:4px;background:var(--gold)}
.sign{position:absolute;left:446px;top:242px;width:370px;height:162px;background:#fff;padding:14px 24px;box-shadow:0 0 30px rgba(255,255,255,.6)}
.sign li{list-style:none;font-size:14px;line-height:35px;display:flex;align-items:center;gap:10px;font-family:"Jost",sans-serif}
.sign li::before{content:"";width:8px;height:8px;border-radius:50%;border:2px solid #333}
.sign .sale{color:var(--accent-red)}
.sign .rent{color:var(--brand-green)}
.hero-arrow{position:absolute;top:253px;width:48px;height:48px;border-radius:50%;background:rgba(255,255,255,.85);display:flex;align-items:center;justify-content:center}
.hero-arrow.prev{left:74px}
.hero-arrow.next{right:74px}
.cta{position:absolute;left:508px;top:437px;width:184px;height:46px;border-radius:23px;background:var(--brand-green);color:#fff;display:flex;align-items:center;justify-content:center;gap:10px;font-family:"Jost",sans-serif;font-size:17px;font-weight:500}
.cta i{width:24px;height:24px;border-radius:50%;background:#fff;display:flex;align-items:center;justify-content:center}

/* what we do */
.what-we-do{height:223px;background:var(--pink);color:#fff;text-align:center;padding-top:42px}
.what-we-do h2{font-size:22px;margin-bottom:14px}
.what-we-do p{width:1052px;margin:0 auto;font-size:13px;line-height:20px}
.more{display:inline-block;margin-top:16px;font-size:13px;font-weight:bold}

/* features */
.features{height:740px;position:relative}
.features h2{text-align:center;font-size:22px;padding-top:42px}
.product-cards{position:absolute;left:65px;top:105px;display:flex;gap:10px}
.card{width:261px;height:458px;margin-top:110px;position:relative;color:#fff}
.card.blue{background:var(--blue)}.card.green{background:var(--green)}.card.yellow{background:var(--yellow)}.card.red{background:var(--red)}
.card-photo{position:absolute;left:36px;top:-110px;width:188px;height:188px;border-radius:50%;overflow:hidden;background:linear-gradient(180deg,#1c2233,#6f7a8c)}
.card-label{position:absolute;left:0;right:0;bottom:0;height:62px;background:rgba(255,255,255,.92);color:#222;text-align:center;font-family:"Jost",sans-serif;font-weight:500;font-size:15px;line-height:17px;padding-top:10px}
.card ul{list-style:none;position:absolute;left:20px;top:138px}
.card li{display:flex;gap:16px;height:90px}
.thumb{width:72px;height:72px;background:#fff;display:flex;align-items:center;justify-content:center}
.thumb span{width:46px;height:46px;background:#c9ced6}
.card p{font-size:14px;line-height:19px;width:140px}
.card .more{margin-top:8px}
.card-foot{position:absolute;bottom:0;left:0;right:0;height:44px;line-height:44px;text-align:center;font-family:"Jost",sans-serif;font-weight:500;font-size:15px}
.blue .card-foot{background:var(--blue-dark)}.green .card-foot{background:var(--green-dark)}.yellow .card-foot{background:var(--yellow-dark)}.red .card-foot{background:var(--red-dark)}

/* perks */
.perks{height:110px;margin:0 auto;width:1052px;border:2px solid var(--gold);border-top:none;position:relative;display:flex;justify-content:space-around;padding:0 110px;top:-52px}
.perks::before{content:"";position:absolute;top:0;left:90px;right:90px;height:2px;background:#fff}
.perks::after{content:"";position:absolute;top:0;left:-2px;right:-2px;height:2px;background:linear-gradient(90deg,var(--gold) 92px,transparent 92px,transparent calc(100% - 92px),var(--gold) calc(100% - 92px))}
.perk{text-align:center;padding-top:0;margin-top:-18px}
.perk svg{display:block;margin:0 auto 8px}
.perk b{font-family:"Jost",sans-serif;font-weight:500;font-size:16px;display:block}
.perk small{font-size:13px;color:#555}

/* why */
.why{height:575px;position:relative;margin-top:-8px}
.why h2,.best h2{font-size:22px}
.why-grid{position:absolute;left:74px;top:0;width:700px}
.why-grid h2{margin-bottom:30px}
.reasons{display:grid;grid-template-columns:360px 340px;row-gap:52px}
.reason{display:flex;gap:18px}
.ring{width:112px;height:112px;border-radius:50%;border:10px solid #e2e2e2;display:flex;align-items:center;justify-content:center;flex:none}
.reason h3{font-size:18px;margin-bottom:6px}
.reason p{font-size:13.5px;line-height:20px;color:#555;width:210px}
.best{position:absolute;left:794px;top:0;width:331px}
.best-head{display:flex;justify-content:space-between;align-items:center;margin-bottom:22px}
.best-head span{display:flex;gap:4px}
.best-head i{width:20px;height:20px;border-radius:50%;border:1px solid #999;display:block}
.seller{display:flex;gap:26px;height:121px}
.seller-thumb{width:92px;height:92px;background:#f0f0f0;display:flex;align-items:center;justify-content:center}
.seller-thumb span{width:54px;height:54px;background:#c5c9cf}
.seller p{font-size:14px;line-height:19px;color:#333;padding-top:6px}
.seller .more{font-size:12px;margin-top:10px;color:#222}

/* newsletter */
.newsletter{height:92px;background:var(--black);color:#fff;position:relative}
.nl-title{position:absolute;left:74px;top:26px;display:flex;gap:12px;align-items:center;font-family:"Jost",sans-serif;font-weight:600;font-size:19px;line-height:20px}
.nl-input{position:absolute;left:340px;top:25px;width:295px;height:42px;border-radius:21px;background:#fff;color:#999;font-size:14px;padding:12px 20px}
.nl-btn{position:absolute;left:642px;top:25px;width:140px;height:42px;border-radius:21px;background:var(--accent-red);font-family:"Jost",sans-serif;font-weight:500;font-size:20px;text-align:center;line-height:42px}
.follow{position:absolute;right:74px;top:30px;display:flex;align-items:center;gap:6px;font-size:13px}
.follow span{margin-right:10px}
.follow i{width:32px;height:32px;border-radius:50%;background:#5a5a5a;display:block}

/* footer */
.site-footer{height:363px;background:var(--footer);position:relative}
.info-boxes{position:absolute;left:74px;top:28px;display:flex;gap:26px}
.info-box{width:334px;height:110px;background:#fff;border:1px solid #ddd;display:flex;gap:18px;padding:14px 16px}
.info-box h4{font-size:14px;font-weight:600;margin-bottom:6px}
.info-box p{font-size:12.5px;line-height:17px;color:#666}
.footer-cols{position:absolute;left:74px;top:160px;display:flex}
.footer-col{width:270px}
.footer-col h4{font-size:13px;font-weight:600;margin-bottom:10px}
.footer-col li{list-style:none;font-size:12.5px;line-height:19px;color:#444}
.footer-col .mail{color:var(--accent-red)}
.legal{position:absolute;left:74px;top:322px;font-size:12px;color:#444}
.payments{position:absolute;right:74px;top:314px;display:flex;align-items:center;gap:6px}
.payments b{font-family:"Jost",sans-serif;font-weight:600;font-size:12px;margin-right:10px}
.payments span{width:48px;height:26px;background:#fff;border:1px solid #ccc;font-size:9px;color:#333;display:flex;align-items:center;justify-content:center}
</style>
</head>
<body>

<header class="site-header">
  <a class="brand" href="#"><span class="brand-dot"></span><span class="brand-name">Solvane Glow LED</span></a>
  <p class="welcome">Welcome, Login or Create an account.</p>
  <nav class="top-links">My Account<span>|</span>Wish List<span>|</span>Checkout<span>|</span>Help</nav>
  <div class="call">
    <svg width="30" height="30" viewBox="0 0 24 24" fill="none" stroke="#3ba846" stroke-width="1.8"><path d="M5 3h4l2 5-2.5 1.5a11 11 0 0 0 6 6L16 13l5 2v4a2 2 0 0 1-2 2A16 16 0 0 1 3 5a2 2 0 0 1 2-2z"/></svg>
    <div><small>Call Us Today</small><strong>1800 55 0142</strong></div>
  </div>
  <a class="cart" href="#">
    <svg width="30" height="30" viewBox="0 0 24 24" fill="none" stroke="#fff" stroke-width="1.8"><path d="M3 9h18l-2 11H5z"/><path d="M8 9l4-6 4 6"/></svg>
    <div><b>Shopping Cart</b><small>(0) item(s) - $0.00</small></div>
  </a>
</header>

<nav class="main-nav">
  <ul>
    <li class="active">LED Billboards</li>
    <li>LED Gas Station lights</li>
    <li>Truss Systems</li>
    <li>Sound Systems</li>
    <li>About Us</li>
    <li>Contact Us</li>
  </ul>
  <div class="search">Search
    <svg width="20" height="20" viewBox="0 0 24 24" fill="none" stroke="#888" stroke-width="2"><circle cx="10" cy="10" r="6"/><path d="M15 15l6 6"/></svg>
  </div>
</nav>

<section class="hero">
  <div class="hero-photo" role="img" aria-label="Night city street with light trails and a lit LED billboard at a bus shelter"></div>
  <h1 class="hero-title">ONE STOP SHOP TO</h1>
  <p class="hero-sub"><i></i>Brighten Your World<i></i></p>
  <ul class="sign">
    <li>LED BILLBOARDS FOR&nbsp;<span class="sale">SALES</span>&nbsp;&amp;&nbsp;<span class="rent">RENT</span></li>
    <li>LED GAS STATION LIGHTS</li>
    <li>TRUSS SYSTEMS FOR&nbsp;<span class="sale">SALES</span>&nbsp;&amp;&nbsp;<span class="rent">RENT</span></li>
    <li>SOUND SYSTEMS FOR&nbsp;<span class="sale">SALES</span>&nbsp;&amp;&nbsp;<span class="rent">RENT</span></li>
  </ul>
  <a class="hero-arrow prev" href="#"><svg width="20" height="20" viewBox="0 0 24 24" fill="none" stroke="#333" stroke-width="3"><path d="M15 5l-7 7 7 7"/></svg></a>
  <a class="hero-arrow next" href="#"><svg width="20" height="20" viewBox="0 0 24 24" fill="none" stroke="#333" stroke-width="3"><path d="M9 5l7 7-7 7"/></svg></a>
  <a class="cta" href="#"><i><svg width="12" height="12" viewBox="0 0 24 24" fill="none" stroke="#3ba846" stroke-width="4"><path d="M9 5l7 7-7 7"/></svg></i>GET STARTED</a>
</section>

<section class="what-we-do">
  <h2>WHAT WE DO</h2>
  <p>Lorem ipsum dolor sit amet, consectetur adipiscing elit, sed do eiusmod tempor incididunt ut labore et dolore magna aliqua. Ut enim ad minim veniam, quis nostrud exercitation ullamco laboris nisi ut aliquip ex ea commodo consequat. Duis aute irure dolor in reprehenderit in voluptate velit esse cillum dolore eu fugiat nulla pariatur. Excepteur sint occaecat cupidatat non proident, sunt in culpa qui officia deserunt mollit anim id est laborum.</p>
  <a class="more" href="#">Learn More ›</a>
</section>

<section class="features">
  <h2>FEATURES FOR MAJOR PRODUCTS</h2>
  <div class="product-cards">
    <article class="card blue">
      <div class="card-photo" role="img" aria-label="Large outdoor billboard at dusk"><div class="card-label">LED<br>BILLBOARDS</div></div>
      <ul>
        <li><div class="thumb"><span></span></div><div><p>Lorem ipsum dolor sit amet, consect.</p><a class="more" href="#">Learn More ›</a></div></li>
        <li><div class="thumb"><span></span></div><div><p>Lorem ipsum dolor sit amet, consect.</p><a class="more" href="#">Learn More ›</a></div></li>
        <li><div class="thumb"><span></span></div><div><p>Lorem ipsum dolor sit amet, consect.</p><a class="more" href="#">Learn More ›</a></div></li>
      </ul>
      <div class="card-foot">SHOW ALL PRODUCTS</div>
    </article>
    <article class="card green">
      <div class="card-photo" role="img" aria-label="Gas station canopy lit at night"><div class="card-label">LED GAS<br>STATION LIGHTS</div></div>
      <ul>
        <li><div class="thumb"><span></span></div><div><p>Lorem ipsum dolor sit amet, consect.</p><a class="more" href="#">Learn More ›</a></div></li>
        <li><div class="thumb"><span></span></div><div><p>Lorem ipsum dolor sit amet, consect.</p><a class="more" href="#">Learn More ›</a></div></li>
        <li><div class="thumb"><span></span></div><div><p>Lorem ipsum dolor sit amet, consect.</p><a class="more" href="#">Learn More ›</a></div></li>
      </ul>
      <div class="card-foot">SHOW ALL PRODUCTS</div>
    </article>
    <article class="card yellow">
      <div class="card-photo" role="img" aria-label="Aluminium stage truss frame" style="background:linear-gradient(180deg,#e9eef3,#a9b2bb)"><div class="card-label">TRUSS<br>SYSTEMS</div></div>
      <ul>
        <li><div class="thumb"><span></span></div><div><p>Lorem ipsum dolor sit amet, consect.</p><a class="more" href="#">Learn More ›</a></div></li>
        <li><div class="thumb"><span></span></div><div><p>Lorem ipsum dolor sit amet, consect.</p><a class="more" href="#">Learn More ›</a></div></li>
        <li><div class="thumb"><span></span></div><div><p>Lorem ipsum dolor sit amet, consect.</p><a class="more" href="#">Learn More ›</a></div></li>
      </ul>
      <div class="card-foot">SHOW ALL PRODUCTS</div>
    </article>
    <article class="card red">
      <div class="card-photo" role="img" aria-label="Audio mixer knobs close up" style="background:linear-gradient(180deg,#d7d9dc,#7b7f85)"><div class="card-label">SOUND<br>SYSTEMS</div></div>
      <ul>
        <li><div class="thumb"><span></span></div><div><p>Lorem ipsum dolor sit amet, consect.</p><a class="more" href="#">Learn More ›</a></div></li>
        <li><div class="thumb"><span></span></div><div><p>Lorem ipsum dolor sit amet, consect.</p><a class="more" href="#">Learn More ›</a></div></li>
        <li><div class="thumb"><span></span></div><div><p>Lorem ipsum dolor sit amet, consect.</p><a class="more" href="#">Learn More ›</a></div></li>
      </ul>
      <div class="card-foot">SHOW ALL PRODUCTS</div>
    </article>
  </div>
</section>

<section class="perks">
  <div class="perk"><svg width="34" height="34" viewBox="0 0 24 24" fill="none" stroke="#666" stroke-width="1.4"><rect x="5" y="3" width="14" height="14" rx="2"/><path d="M5 10h14M8 20v-3M16 20v-3"/></svg><b>FREE SHIPPING</b><small>On over order $99</small></div>
  <div class="perk"><svg width="34" height="34" viewBox="0 0 24 24" fill="none" stroke="#666" stroke-width="1.4"><circle cx="14" cy="7" r="4"/><path d="M2 18h5l6 2 8-4-2-2-6 2"/></svg><b>100% MONEY BACK</b><small>Guarantee</small></div>
  <div class="perk"><svg width="34" height="34" viewBox="0 0 24 24" fill="none" stroke="#666" stroke-width="1.4"><path d="M10 2l2 5 5 .5-4 3.5 1.3 5L10 13l-4.3 3 1.3-5-4-3.5L8 7z"/><circle cx="17" cy="18" r="4"/></svg><b>HIGH QUALITY</b><small>Products</small></div>
  <div class="perk"><svg width="34" height="34" viewBox="0 0 24 24" fill="none" stroke="#666" stroke-width="1.4"><path d="M5 13a7 7 0 0 1 14 0"/><rect x="3" y="12" width="4" height="6" rx="1"/><rect x="17" y="12" width="4" height="6" rx="1"/><path d="M19 18v1a3 3 0 0 1-3 3h-3"/></svg><b>CUSTOMER SUPPORT</b><small>We are here for you</small></div>
</section>

<section class="why">
  <div class="why-grid">
    <h2>WHY CHOOSE US?</h2>
    <div class="reasons">
      <div class="reason"><div class="ring"><svg width="40" height="40" viewBox="0 0 24 24" fill="none" stroke="#888" stroke-width="1.6"><rect x="6" y="6" width="12" height="12"/><path d="M9 2v4M15 2v4M9 18v4M15 18v4M2 9h4M2 15h4M18 9h4M18 15h4"/></svg></div><div><h3>TECHNOLOGY</h3><p>Lorem ipsum dolor sit amet, do consectetuer elit rem ipsum sit amet, consectetuer elitctetuer elit rem ipsum sit amet.</p></div></div>
      <div class="reason"><div class="ring"><svg width="40" height="40" viewBox="0 0 24 24" fill="none" stroke="#888" stroke-width="1.8"><rect x="4" y="4" width="16" height="16"/><path d="M8 12l3 3 8-9"/></svg></div><div><h3>QUALITY</h3><p>Lorem ipsum dolor sit amet, do consectetuer elit rem ipsum sit amet, consectetuer elitctetuer elit rem ipsum sit amet.</p></div></div>
      <div class="reason"><div class="ring"><svg width="40" height="40" viewBox="0 0 24 24" fill="none" stroke="#888" stroke-width="1.8"><circle cx="12" cy="12" r="9"/><path d="M8 16l8-8"/><circle cx="9" cy="9" r="1.2"/><circle cx="15" cy="15" r="1.2"/></svg></div><div><h3>PRICE</h3><p>Lorem ipsum dolor sit amet, do consectetuer elit rem ipsum sit amet, consectetuer elitctetuer elit rem ipsum sit amet.</p></div></div>
      <div class="reason"><div class="ring"><svg width="40" height="40" viewBox="0 0 24 24" fill="#888"><path d="M12 2l3 7 7 .6-5.3 4.7 1.6 7L12 17.6 5.7 21.3l1.6-7L2 9.6 9 9z"/></svg></div><div><h3>WARRANTY</h3><p>Lorem ipsum dolor sit amet, do consectetuer elit rem ipsum sit amet, consectetuer elitctetuer elit rem ipsum sit amet.</p></div></div>
      <div class="reason"><div class="ring"><svg width="40" height="40" viewBox="0 0 24 24" fill="none" stroke="#888" stroke-width="2.4"><circle cx="12" cy="12" r="3"/><circle cx="12" cy="12" r="7" stroke-dasharray="3 2.5"/></svg></div><div><h3>SERVICE</h3><p>Lorem ipsum dolor sit amet, do consectetuer elit rem ipsum sit amet, consectetuer elitctetuer elit rem ipsum sit amet.</p></div></div>
      <div class="reason"><div class="ring"><svg width="40" height="40" viewBox="0 0 24 24" fill="none" stroke="#888" stroke-width="1.8"><path d="M5 13a7 7 0 0 1 14 0"/><rect x="3" y="12" width="4" height="6" rx="1"/><rect x="17" y="12" width="4" height="6" rx="1"/></svg></div><div><h3>SUPPORT</h3><p>Lorem ipsum dolor sit amet, do consectetuer elit rem ipsum sit amet, consectetuer elitctetuer elit rem ipsum sit amet.</p></div></div>
    </div>
  </div>
  <aside class="best">
    <div class="best-head"><h2>BEST SELLERS</h2><span><i></i><i></i></span></div>
    <div class="seller"><div class="seller-thumb"><span></span></div><div><p>Lorem ipsum dolor sit amet, consectetuer elit</p><a class="more" href="#">Learn More ›</a></div></div>
    <div class="seller"><div class="seller-thumb"><span></span></div><div><p>Lorem ipsum dolor sit amet, consectetuer elit</p><a class="more" href="#">Learn More ›</a></div></div>
    <div class="seller"><div class="seller-thumb"><span></span></div><div><p>Lorem ipsum dolor sit amet, consectetuer elit</p><a class="more" href="#">Learn More ›</a></div></div>
    <div class="seller"><div class="seller-thumb"><span></span></div><div><p>Lorem ipsum dolor sit amet, consectetuer elit</p><a class="more" href="#">Learn More ›</a></div></div>
  </aside>
</section>

<section class="newsletter">
  <div class="nl-title"><svg width="70" height="36" viewBox="0 0 70 36" fill="none" stroke="#bbb" stroke-width="2"><rect x="24" y="4" width="42" height="28"/><path d="M24 4l21 16 21-16"/><path d="M2 12h16M8 20h12M4 28h14"/></svg><span>SUBSCRIBE<br>OUR NEWSLETTER</span></div>
  <div class="nl-input">Enter Your Email</div>
  <a class="nl-btn" href="#">SUBSCRIBE</a>
  <div class="follow"><span>FOLLOW US</span><i></i><i></i><i></i><i></i><i></i></div>
</section>

<footer class="site-footer">
  <div class="info-boxes">
    <div class="info-box"><svg width="56" height="60" viewBox="0 0 24 26" fill="none" stroke="#888" stroke-width="1.3"><rect x="3" y="2" width="15" height="20"/><path d="M6 7h9M6 11h9M6 15h5"/><path d="M13 19l3 3 6-7"/></svg><div><h4>PRODUCT CATALOGUE</h4><p>It was popularised in the 1960s with the release of Lettaform sheets inuding versions of Loarem Ipsum.</p></div></div>
    <div class="info-box"><svg width="56" height="60" viewBox="0 0 24 26" fill="none" stroke="#888" stroke-width="1.3"><path d="M3 5h14v10H9l-4 4v-4H3z"/><path d="M19 9h3v9h-2v3l-3-3h-6v-2"/></svg><div><h4>SOLVANE GLOW LED BLOGS</h4><p>It was popularised in the 1960s with the release of Lettaform sheets inuding versions of Loarem Ipsum.</p></div></div>
    <div class="info-box"><svg width="56" height="60" viewBox="0 0 24 26" fill="none" stroke="#888" stroke-width="1.3"><rect x="3" y="3" width="14" height="20"/><path d="M6 8h8M6 12h8M6 16h5"/><path d="M21 4l-7 12-1 3 3-1 7-12z"/></svg><div><h4>GUIDES &amp; ADVISE</h4><p>It was popularised in the 1960s with the release of Lettaform sheets inuding versions of Loarem Ipsum.</p></div></div>
  </div>
  <div class="footer-cols">
    <div class="footer-col"><h4>SHOP BY CATEGORIES</h4><ul><li>LED Billboards for Sale &amp; Rent</li><li>LED Gas Station lights</li><li>Truss Systems for Sale &amp; Rent</li><li>Sound Systems for Sale &amp; Rent</li></ul></div>
    <div class="footer-col"><h4>CUSTOMER SERVICE</h4><ul><li>Contact Us</li><li>Returns</li><li>Site Map</li><li>Delivery info</li></ul></div>
    <div class="footer-col"><h4>MY ACCOUNT</h4><ul><li>Order History</li><li>Wish List</li><li>Newsletter</li><li>Gift Voucher</li></ul></div>
    <div class="footer-col"><h4>STORE LOCATION</h4><ul><li>8646 Address name, City name, State<br>name 9078, Country name</li><li style="margin-top:6px">1800 55 0177</li><li class="mail">info@solvaneglowled.test</li></ul></div>
  </div>
  <p class="legal">© 2016 Solvane Glow LED. All Rights Reserved. Terms of Use | Privacy Policy</p>
  <div class="payments"><b>PAYMENT OPTIONS</b><span>Cardora</span><span>Paywell</span><span>Mintcard</span><span>Amberpay</span><span>Dayspend</span></div>
</footer>

</body>
</html>
```